Solution Brief Design for Analytics Start-Up

We need a 1-page (front and back) solution brief design to showcase our analytics products and services. Our initial use will be for advisory services designed to help customers chart a path to becoming analytics-driven.
We have uploaded a draft version of flyer to give you an idea elements that need to be included. You do not need to copy the structure or layout, as we are counting on your creativity to improve the elements and layout as need to create a professional, visually attractive, and easy to read document.
Target Market(s)
Our target audience for the solution briefs include sales and marketing chiefs, CFOs, CIOs, and CEOs, in corporations of all industries ranging from $100 million to $10+ billion in revenues.
Requirements
Must have
- The flyer should be 1 page, with design and copy on front and back. The colors should match our logo and website www.corvantix512.com
- It should include the attached VEX Framework Graphic.
- Have sections for main text and sections for call-outs on front and back.
Nice to have
- Create a better looking version of our VEX Framework graphic.
- Include a header similar to the main banner photo on our website.
- Add some relevant and compelling photos or graphics.
Should not have
- No light bulbs. No old-style fonts.

```html
<!DOCTYPE html>
<html lang="en">
<head>
<meta charset="utf-8">
<title>Corvantix512 Solution Brief</title>
<link rel="stylesheet" href="https://fonts.googleapis.com/css2?family=Didact+Gothic&family=Roboto+Condensed:wght@400;500&family=Arimo:wght@700&display=swap">
<style>
  :root {
    --page-bg: #e9e9ea;
    --paper: #ffffff;
    --navy: #1f3a8a;
    --royal: #2a5fb0;
    --headline-blue: #2b6cb3;
    --gold: #8c7a3c;
    --text: #3b3b3b;
    --bullet-red: #d23a2c;
    --bullet-blue: #3f8fd6;
    --callout-bg: #b3e1e6;
  }
  * { box-sizing: border-box; margin: 0; padding: 0; }
  html, body { width: 890px; height: 1200px; overflow: hidden; background: var(--page-bg); }
  body { position: relative; font-family: "Didact Gothic", "Century Gothic", sans-serif; color: var(--text); }

  .brief {
    position: absolute; left: 30px; top: 13px; width: 830px; height: 1174px;
    background: var(--paper); overflow: hidden;
    box-shadow: 0 2px 10px rgba(0,0,0,.18);
  }
  .swoosh { position: absolute; left: 0; width: 830px; }
  .swoosh--top { top: 0; height: 140px; }
  .swoosh--bottom { bottom: 0; height: 110px; }

  .brand { position: absolute; right: 40px; top: 56px; text-align: right; }
  .brand__name {
    font-family: "Didact Gothic", sans-serif; font-size: 38px;
    color: var(--navy); line-height: 1;
  }
  .brand__tagline {
    font-family: "Didact Gothic", sans-serif; font-size: 16px;
    color: var(--gold); margin-top: 10px;
  }

  .hero {
    position: absolute; left: 28px; top: 143px; width: 775px; height: 333px;
    border: 1.5px solid var(--gold); border-radius: 22px;
  }
  .hero__headline {
    position: absolute; left: 10px; top: 36px; width: 330px; text-align: center;
    font-weight: 400; font-size: 28px; line-height: 39px; color: var(--headline-blue);
    white-space: nowrap;
  }
  .hero__photo {
    position: absolute; left: 344px; top: 11px; width: 416px; height: 310px;
    background: linear-gradient(160deg, #dfe6ec 0%, #c9d3dc 35%, #b88a5e 70%, #8e5f3a 100%);
  }

  .body-col { position: absolute; font-size: 12.9px; letter-spacing: .25px; line-height: 19.5px; text-align: justify; }
  .body-col--left { left: 40px; top: 490px; width: 362px; }
  .body-col--left p + p { margin-top: 19px; }

  .questions { list-style: none; margin: 30px 0 0 30px; }
  .questions li { position: relative; margin-bottom: 18px; line-height: 18px; }
  .questions li::before {
    content: ""; position: absolute; left: -22px; top: 4px; width: 10px; height: 10px;
    border-radius: 50%; background: radial-gradient(circle at 35% 35%, #f27a6c, var(--bullet-red));
  }

  .body-col--right { left: 428px; top: 497px; width: 360px; line-height: 16.6px; }
  .section-title {
    font-family: "Roboto Condensed", sans-serif; font-weight: 500; font-size: 19px;
    letter-spacing: 0; color: var(--royal); line-height: 1.2; margin-bottom: 6px;
    text-align: left; white-space: nowrap;
  }
  .outcomes { list-style: none; margin: 20px 0 0 30px; }
  .outcomes li { position: relative; margin-bottom: 15px; line-height: 15px; }
  .outcomes li::before {
    content: ""; position: absolute; left: -17px; top: 2px; width: 10px; height: 10px;
    border-radius: 50%; background: radial-gradient(circle at 35% 35%, #9cd0f5, var(--bullet-blue));
  }

  .highlights {
    position: absolute; left: 417px; top: 788px; width: 384px; height: 286px;
    background: var(--callout-bg); border-radius: 18px; padding: 18px 10px 0 12px;
    font-size: 12.9px; letter-spacing: .25px; line-height: 15px;
  }
  .highlights .section-title { margin-bottom: 14px; }
  .highlights ul { list-style: none; }
  .highlights li { display: flex; gap: 10px; margin-bottom: 16px; text-align: justify; }
  .highlights svg { flex: 0 0 18px; width: 18px; height: 16px; margin-top: 1px; }

  .contact {
    position: absolute; left: 40px; right: 40px; bottom: 20px;
    display: flex; align-items: center; justify-content: space-between;
    font-family: "Arimo", Arial, sans-serif; font-weight: 700; font-size: 13.4px; color: #fff;
  }
  .contact__sep { width: 7px; height: 7px; border-radius: 50%; background: #fff; opacity: .85; }
</style>
</head>
<body>
  <main class="brief">
    <svg class="swoosh swoosh--top" viewBox="0 0 830 140" preserveAspectRatio="none" aria-hidden="true">
      <defs>
        <linearGradient id="topBlue" x1="0" y1="0" x2="1" y2="1">
          <stop offset="0" stop-color="#2e6fc0"/>
          <stop offset="1" stop-color="#1d3a8a"/>
        </linearGradient>
      </defs>
      <path d="M0 105 C 150 118, 320 90, 470 0 L 0 0 Z" fill="#c9ccd2"/>
      <path d="M0 92 C 150 102, 320 80, 472 0 L 0 0 Z" fill="url(#topBlue)"/>
    </svg>

    <header class="brand">
      <div class="brand__name">Corvantix512</div>
      <div class="brand__tagline">Analytics advisory for growing teams</div>
    </header>

    <section class="hero">
      <h1 class="hero__headline">Maximizing the<br>value of your<br>information assets<br>and accelerating<br>your business<br>performance through<br>advanced analytics</h1>
      <div class="hero__photo" role="img" aria-label="Photo of a business team in a meeting room with a presenter at a flip chart"></div>
    </section>

    <section class="body-col body-col--left">
      <p>Advanced analytics is helping companies accelerate their business performance and enhance their competitive edge in business growth, margin, and market share. It helps organizations generate insight from potentially massive amounts of data through variety of sources. Insight can be real-time, predictive, and is integrated into business processes and actions. Advanced analytics can lead to better customer experience, improved quality, and more clear understanding of risks in business execution.</p>
      <p>The first steps in your accelerated journey to become more data driven are understanding the analytics opportunities available and their fit with your organizational capabilities, resources, and, most importantly, business priorities. If you are just starting to look into what advanced analytics can do for you and your organization, you may be asking:</p>
      <ul class="questions">
        <li>What are our top business priorities and how can advanced analytics help us achieve them?</li>
        <li>Where should I start? What are my top opportunities and use cases for deploying advanced analytics in my company?</li>
        <li>What business benefits can I gain through more focused investment in analytics? How does it help me address my business priorities?</li>
        <li>How can I accelerate my analytics initiatives to gain competitive edge?</li>
      </ul>
    </section>

    <section class="body-col body-col--right">
      <h2 class="section-title">The Value of Evaluating Analytics Opportunities</h2>
      <p>Assessing potential analytics opportunities guides your decision on where to start with your data transformation. It helps you make more informed decision on where to focus and apply your investments and resources, with highest chances of positive business impact. This enables you to ultimately:</p>
      <ul class="outcomes">
        <li>Undertake the transformation to become more data driven, by incorporating advanced analytics in your business processes</li>
        <li>Extend the reach of your existing analytics initiatives and enrich the insight across your organization</li>
        <li>Use data and analytics to achieve business objectives and gain true competitive edge</li>
      </ul>
    </section>

    <aside class="highlights">
      <h2 class="section-title">Highlights</h2>
      <ul>
        <li><svg viewBox="0 0 18 16" aria-hidden="true"><rect x="1" y="3" width="12" height="12" fill="none" stroke="#2a5fb0" stroke-width="1.6"/><path d="M4 8 L7.5 12 L17 1" fill="none" stroke="#2a5fb0" stroke-width="2.4"/></svg><span>Advanced analytics accelerates business growth through insight that is relevant, predictive, and leads to action</span></li>
        <li><svg viewBox="0 0 18 16" aria-hidden="true"><rect x="1" y="3" width="12" height="12" fill="none" stroke="#2a5fb0" stroke-width="1.6"/><path d="M4 8 L7.5 12 L17 1" fill="none" stroke="#2a5fb0" stroke-width="2.4"/></svg><span>Analyze potential analytics opportunities and their fit/gap against your business priorities and capabilities</span></li>
        <li><svg viewBox="0 0 18 16" aria-hidden="true"><rect x="1" y="3" width="12" height="12" fill="none" stroke="#2a5fb0" stroke-width="1.6"/><path d="M4 8 L7.5 12 L17 1" fill="none" stroke="#2a5fb0" stroke-width="2.4"/></svg><span>Validate opportunities with key stakeholders to ensure alignment</span></li>
        <li><svg viewBox="0 0 18 16" aria-hidden="true"><rect x="1" y="3" width="12" height="12" fill="none" stroke="#2a5fb0" stroke-width="1.6"/><path d="M4 8 L7.5 12 L17 1" fill="none" stroke="#2a5fb0" stroke-width="2.4"/></svg><span>Rank top opportunities and identify business case and ROI drivers through use cases</span></li>
        <li><svg viewBox="0 0 18 16" aria-hidden="true"><rect x="1" y="3" width="12" height="12" fill="none" stroke="#2a5fb0" stroke-width="1.6"/><path d="M4 8 L7.5 12 L17 1" fill="none" stroke="#2a5fb0" stroke-width="2.4"/></svg><span>Identify potential execution risks and mitigation strategies</span></li>
      </ul>
    </aside>

    <svg class="swoosh swoosh--bottom" viewBox="0 0 830 110" preserveAspectRatio="none" aria-hidden="true">
      <defs>
        <linearGradient id="bandBlue" x1="0" y1="0" x2="0" y2="1">
          <stop offset="0" stop-color="#2e66b5"/>
          <stop offset="1" stop-color="#1e3c8c"/>
        </linearGradient>
      </defs>
      <path d="M0 0 C 120 30, 300 40, 520 30 C 660 24, 760 18, 830 14 L 830 110 L 0 110 Z" fill="#c4c7cd"/>
      <path d="M0 24 C 140 46, 320 52, 520 42 C 660 36, 760 30, 830 26 L 830 110 L 0 110 Z" fill="url(#bandBlue)"/>
    </svg>

    <footer class="contact">
      <span>1820 Harlow Drive, Suite 300</span>
      <span class="contact__sep"></span>
      <span>info@corvantix512.com</span>
      <span class="contact__sep"></span>
      <span>1.555.014.2290</span>
      <span class="contact__sep"></span>
      <span>www.corvantix512.com</span>
    </footer>
  </main>
</body>
</html>
```